Marketing Flyer for Office Space for Lease

I am looking for a pretty standard and professional real estate flyer listing my property for lease. I am not looking for anything over the top creative, just something very professional looking. The building address is 4817 E. Calloway Avenue, Lauderhill, FL 33319. I included some sample flyers of what other companies use as examples on what I am looking for. Please use the attached Dorvel Holdings Realty logo, but remove the long line after it extends past the words. I also included a Word file that gives you the building information and marketing information. Please use the photos attached in the zipped folder as you see fit.
Updates

Project Deadline Extended
Reason: I am getting updated building measurements next Thursday. I want to be able to give these figures to you to ensure the flyer is final. I will keep making comments on the rest of the designs while I wait for those numbers. Thank you.

Project Deadline Extended
Reason: Just got the floor plans, so I needed to adjust the figures on the flyer. Otherwise I would just have an incorrect flyer.

Target Market(s)

Businesses that would want to lease space in this building.

Industry/Entity Type

Real Estate

Font styles to use
Serif
Sans Serif

Colors

Designer to choose colors to be used in the design.

Requirements
Must have
• Building photo, address, map, and building highlights from the Word file.
Nice to have
• I included the example flyers that I have seen or used in the past. Taking ideas from there could work well.
Should not have
• Crazy big fonts, crazy colors, hard to read fonts, too wild of layout.

```html
<!DOCTYPE html>
<html lang="en">
<head>
<meta charset="utf-8">
<title>For Lease – 4817 E. Calloway Avenue</title>
<link href="https://fonts.googleapis.com/css2?family=Roboto+Condensed:wght@400;700&display=swap" rel="stylesheet">
<style>
  :root {
    --navy: #22508f;
    --navy-dark: #1c4580;
    --sky: #1ea3dd;
    --title: #234f8c;
    --ink: #333842;
    --panel-top: #f4f4f4;
    --panel-bottom: #dcdcdc;
    --white: #ffffff;
  }
  * { box-sizing: border-box; margin: 0; padding: 0; }
  html, body { width: 928px; height: 1200px; overflow: hidden; background: var(--white); }
  body { font-family: "Roboto Condensed", "Arial Narrow", sans-serif; color: var(--ink); }
  .flyer { position: relative; width: 928px; height: 1200px; overflow: hidden; background: var(--white); }

  .masthead { position: absolute; left: 0; top: 0; width: 928px; height: 80px; }
  .masthead svg { position: absolute; left: 0; top: 0; }
  .masthead h1 {
    position: absolute; left: 0; top: 14px; width: 100%; text-align: center;
    color: var(--white); font-weight: 400; font-size: 36px; letter-spacing: -0.2px;
  }
  .masthead h1 strong { font-weight: 700; }

  .hero-photo {
    position: absolute; left: 0; top: 80px; width: 928px; height: 450px;
    background: linear-gradient(180deg, #6fa6d8 0%, #b9d3ea 30%, #e9eef1 52%, #8f969c 78%, #3b3f45 100%);
  }

  .stats { position: absolute; left: 0; top: 530px; width: 928px; height: 67px; display: flex; }
  .stat {
    color: var(--white); text-align: center; font-size: 20px; line-height: 27px;
    padding-top: 7px; background: var(--navy);
  }
  .stat b { font-weight: 700; }
  .stat.total { width: 341px; }
  .stat.vacant { width: 246px; background: var(--sky); }
  .stat.floors { width: 341px; }

  .details {
    position: absolute; left: 0; top: 597px; width: 398px; height: 603px;
    background: linear-gradient(90deg, var(--panel-top) 0%, #ececec 70%, var(--panel-bottom) 100%);
  }
  .property-name {
    position: absolute; left: 80px; top: 34px; color: var(--title);
    font-weight: 700; font-size: 38px; line-height: 44px;
  }
  .property-address { position: absolute; left: 80px; top: 143px; font-size: 22px; line-height: 30px; }
  .contact { position: absolute; left: 80px; top: 220px; font-size: 20px; line-height: 28px; }
  .contact .phone { font-size: 22px; }
  .contact .phone b { color: var(--title); font-weight: 700; }
  .location-map {
    position: absolute; left: 46px; top: 320px; width: 352px; height: 250px;
    background: linear-gradient(135deg, #eef0ee 0%, #e3e6e2 60%, #dde3e8 100%);
  }

  .features { position: absolute; left: 448px; top: 624px; width: 440px; }
  .features h2 {
    display: inline-block; background: var(--navy); color: var(--white);
    font-weight: 400; font-size: 26px; line-height: 33px; padding: 0 16px;
  }
  .features ul { list-style: none; margin-top: 7px; }
  .features li {
    position: relative; padding-left: 15px; font-size: 19px; line-height: 23px; margin-bottom: 4px;
  }
  .features li::before {
    content: ""; position: absolute; left: 2px; top: 9px; width: 5px; height: 5px;
    border-radius: 50%; background: var(--sky);
  }

  .brand {
    position: absolute; left: 468px; top: 1098px; color: var(--navy);
    font-weight: 700; font-size: 32px; letter-spacing: 1px;
  }

  .corner { position: absolute; right: 0; bottom: 0; }
</style>
</head>
<body>
<div class="flyer">
  <header class="masthead">
    <svg width="928" height="80" viewBox="0 0 928 80" aria-hidden="true">
      <rect width="928" height="80" fill="var(--navy)"/>
      <polygon points="0,72 928,72 928,80 0,80" fill="var(--white)"/>
      <polygon points="0,72 520,78 928,72 928,80 0,80" fill="var(--sky)"/>
    </svg>
    <h1><strong>FOR LEASE</strong> 4817 E. Calloway Avenue</h1>
  </header>

  <div class="hero-photo" role="img" aria-label="Photo of the white three-storey office building with blue accent, palm trees and front parking lot under a blue sky"></div>

  <section class="stats">
    <div class="stat total">Total Building Size:<br><b>42,040 SF</b></div>
    <div class="stat vacant">Vacant Space:<br><b>38,000 SF</b></div>
    <div class="stat floors">1st and 2nd floor sizes:<br><b>about 15,500 each</b></div>
  </section>

  <aside class="details">
    <h2 class="property-name">4817 East<br>Calloway Ave</h2>
    <p class="property-address">4817 E. Calloway Avenue,<br>Lauderhill, FL 33319</p>
    <div class="contact">
      <p>Contact us</p>
      <p class="phone">T. <b>561–555–0142</b></p>
      <p>E. leasing@dorvelholdings.com</p>
    </div>
    <div class="location-map" role="img" aria-label="Street map of Lauderhill showing the building location near the main boulevard"></div>
  </aside>

  <section class="features">
    <h2>Key features</h2>
    <ul>
      <li>New landlord purchased building recently and is moving into half of 3rd floor. Rest of building is vacant. New tenants can pick any location in the building they would like.</li>
      <li>Can accommodate a tenant up to 30,000 SF</li>
      <li>Monument signage available</li>
      <li>Located right on Calloway Avenue and a few blocks away from busiest intersection in all of Broward County of Calloway and US 441.</li>
      <li>Parking ratio over 5 per 1,000 SF including secured, private parking in rear of building.</li>
      <li>Negotiable tenant improvement allowances.</li>
      <li>Competitive rental rates.</li>
      <li>On–site management.</li>
      <li>Can accommodate professional or medical offices.</li>
    </ul>
  </section>

  <div class="brand">DORVEL HOLDINGS REALTY</div>

  <svg class="corner" width="928" height="80" viewBox="0 0 928 80" aria-hidden="true">
    <polygon points="830,80 928,18 928,80" fill="var(--navy-dark)"/>
    <rect x="450" y="75" width="478" height="5" fill="var(--navy-dark)"/>
  </svg>
</div>
</body>
</html>
```